Tri Fold - Restaurant Brochure & pdf multipage

Develop a product guide specific to "restaurant owners" for our company's restaurant insurance services. It will need to be eye-catching, personal, unique, and industry-specific. Several Insurance flyers from our companies are attached for review. We are happy to provide guidance along the way. Our website is www.kovalenbrokerage.example. Please grab logos etc. from there. We can provide other files and more detailed copy.

Target Market(s)

Restaurant owners and CFO's

Industry/Entity Type

Insurance Broker

Font styles to use
Other font styles liked:
• match website fonts

Requirements
Must have
• WE WILL PROVIDE DETAILED CONTENT! AT THIS TIME WE ARE LOOKING FOR THE BASIC DESIGN AND LAYOUT.

EYE-CATCHING MODERN DESIGN WITH IMAGES AND BRANDED FEEL. must be print-ready and set up as a PDF to email.

brief description of our agency and its personal boutique feel specializing in the restaurant market. Also, offer a full-service solution to no only manage their business but personal risks too.

Coverages that need to be listed with a brief description: (See attached Flyers)
General Liability
FF&E (Furniture, Fixtures, and Equipment), Property
Workers Compensation
Umbrella
Liquor Liability
Auto
Cyber
Bonds
EPLI

Carrier List:
The Wexmoor
Bastion
Ferrow Common
Wayfarers
Plains Motor
Quorra
DELVA
Holloway
CountyFirst
KTO
And many more
Nice to have
• carrier logos if room.
Should not have
• TO BE DETERMINED.

```html
<!DOCTYPE html>
<html lang="en">
<head>
<meta charset="utf-8">
<title>Kovalen Insurance Group – Restaurant Brochure</title>
<link href="https://fonts.googleapis.com/css2?family=Montserrat:wght@400;500;600;700;800&display=swap" rel="stylesheet">
<style>
:root{
  --red:#e4232b;
  --red-deep:#b3141b;
  --orange:#f04a24;
  --ink:#2b2b2b;
  --text:#3d3d3d;
  --paper:#ffffff;
  --backdrop:#e9ebe9;
}
*{margin:0;padding:0;box-sizing:border-box}
html,body{width:1200px;height:961px;overflow:hidden;background:var(--backdrop);font-family:"Montserrat",sans-serif;color:var(--text)}
.page{position:absolute;top:118px;width:553px;height:716px;background:var(--paper);overflow:hidden}
.page--about{left:36px}
.page--coverage{left:611px}
.page-art{position:absolute;inset:0}
.footer-band{position:absolute;left:0;right:0;bottom:0;height:18px;background:linear-gradient(90deg,var(--red),var(--orange))}

/* about page */
.brand{position:absolute;left:100px;top:96px;color:#fff;font-weight:700}
.brand-name{display:flex;align-items:center;gap:10px;font-size:38px;letter-spacing:1px;line-height:1}
.brand-mark{width:26px;height:26px;background:var(--red)}
.brand-sub{font-size:14px;letter-spacing:4px;margin-top:8px}
.brand-tag{font-size:6px;letter-spacing:2px;margin-top:3px}
.heading-about{position:absolute;left:17px;top:472px;font-size:40px;line-height:1;font-weight:800;color:var(--red);letter-spacing:.5px}
.about-copy{position:absolute;left:16px;top:522px;width:238px;font-size:7.4px;line-height:1.32}
.about-copy p{margin-bottom:8px}
.heading-service{position:absolute;left:289px;top:562px;font-size:19px;line-height:1;font-weight:800;color:var(--red)}
.service-copy{position:absolute;left:289px;top:588px;width:250px;font-size:7.4px;line-height:1.32}

/* coverage page */
.heading-coverage{position:absolute;left:34px;top:170px;font-size:28px;line-height:1.16;font-weight:800;color:var(--red);letter-spacing:.3px}
.coverage{position:absolute;display:flex;gap:6px;width:245px}
.coverage-icon{flex:none;width:53px;height:53px;background:var(--red);display:flex;align-items:center;justify-content:center}
.coverage-icon svg{width:34px;height:34px;fill:none;stroke:#fff;stroke-width:2;stroke-linecap:round;stroke-linejoin:round}
.coverage h3{font-size:14.5px;font-weight:700;color:var(--ink);margin-top:-2px;margin-bottom:4px}
.coverage p{font-size:7px;line-height:1.3}
.carriers{position:absolute;left:34px;top:578px;width:487px;height:103px;border:2.5px solid var(--red);border-radius:14px}
.carriers-title{position:absolute;left:60px;top:-14px;padding:0 10px;background:var(--paper);font-size:18px;font-weight:800;color:var(--red)}
.carrier-grid{position:absolute;inset:12px 8px 8px;display:grid;grid-template-columns:repeat(6,1fr);grid-template-rows:1fr 1fr;align-items:center;justify-items:center}
.carrier{font-size:9.5px;font-weight:700;color:#3a4a5c;text-align:center;line-height:1.1}
</style>
</head>
<body>

<section class="page page--about">
  <svg class="page-art" viewBox="0 0 553 716" aria-hidden="true">
    <defs>
      <linearGradient id="room" x1="0" y1="0" x2="1" y2="1">
        <stop offset="0" stop-color="#3a2a24"/><stop offset=".5" stop-color="#7a4a35"/><stop offset="1" stop-color="#2d2b2b"/>
      </linearGradient>
      <linearGradient id="swoosh" x1="0" y1="0" x2="1" y2="1">
        <stop offset="0" stop-color="#f04a24"/><stop offset="1" stop-color="#b3141b"/>
      </linearGradient>
    </defs>
    <rect width="553" height="500" fill="url(#room)"/>
    <path d="M0 0 H300 C180 40 80 120 0 240 Z" fill="url(#swoosh)" opacity=".9"/>
    <path d="M553 0 V150 C520 90 480 40 420 0 Z" fill="url(#swoosh)"/>
    <path d="M0 230 C150 270 330 300 553 330 V440 C380 410 200 390 0 370 Z" fill="url(#swoosh)"/>
    <path d="M0 400 C150 375 320 400 553 460 V716 H0 Z" fill="#fff"/>
  </svg>
  <div role="img" aria-label="Photo of a smiling restaurant owner in an apron, arms crossed" style="position:absolute;left:330px;top:20px;width:223px;height:430px;background:linear-gradient(180deg,#d8cfc8,#6e2a2e 60%,#4a3a38);clip-path:polygon(20% 0,100% 0,100% 100%,35% 88%,0 45%)"></div>

  <div class="brand">
    <div class="brand-name">KOVALEN<span class="brand-mark"></span></div>
    <div class="brand-sub">INSURANCE GROUP</div>
    <div class="brand-tag">RESTAURANT RISK SPECIALISTS</div>
  </div>

  <svg class="page-art" viewBox="0 0 553 716" aria-hidden="true">
    <g fill="none" stroke="var(--red)" stroke-width="6" stroke-linecap="round">
      <path d="M52 410 A70 70 0 0 0 188 410"/>
      <path d="M232 440 A70 70 0 0 0 368 440"/>
      <path d="M394 500 A62 62 0 0 0 514 500"/>
    </g>
  </svg>
  <div role="img" aria-label="Photo of a large family home at dusk" style="position:absolute;left:65px;top:339px;width:110px;height:110px;border-radius:50%;border:3px solid #fff;background:linear-gradient(180deg,#d88aa0,#6a6e8a 55%,#5a4a3a)"></div>
  <div role="img" aria-label="Photo of a dark sedan parked outside a house" style="position:absolute;left:240px;top:366px;width:120px;height:120px;border-radius:50%;border:3px solid #fff;background:linear-gradient(180deg,#6f8f5a,#2c3e5a 70%,#8a8a8a)"></div>
  <div role="img" aria-label="Photo of a man washing a classic blue car" style="position:absolute;left:402px;top:438px;width:104px;height:104px;border-radius:50%;border:3px solid #fff;background:linear-gradient(180deg,#c9a080,#3a6aa8 60%,#9ab0c8)"></div>

  <h1 class="heading-about">ABOUT</h1>
  <div class="about-copy">
    <p>Kovalen Insurance group is an independently owned risk management firm with offices located in Maplestone, Georgia, at Lake Verrin and thriving Downtown Ashford Ridge, Georgia. The firm was formed in 2010 and has helped countless families and businesses in Georgia receive the best risk management service.</p>
    <p>Restaurant business owners policy offers an affordable way for you to obtain property and liability insurance. This policy includes key coverages that are important to any business, and also offers additional business-specific options that are essential for any restaurant</p>
    <p>Our clients can access personalized insurance plans at competitive prices and with complete coverage. We work with a multitude of A rated or better insurance carriers for commercial and affluent personal risks.</p>
  </div>
  <h2 class="heading-service">FULL-SERVICE SOLUTION</h2>
  <p class="service-copy">We provide affluent individuals and their families with complete risk management solutions to protect their assets and lifestyle. We take a personal interest and make an effort to understand each of your expectations and needs. Once we have clearly understood and agreed about your needs, we will provide you with a program that is custom-tailored to your individual situation. We are committed to providing comprehensive risk management solutions to ensure that you do not have any gaps in your program and that you receive maximum coverage for your every dollar.</p>
  <div class="footer-band"></div>
</section>

<section class="page page--coverage">
  <div role="img" aria-label="Motion-blurred photo of a car wheel on a road at sunset" style="position:absolute;left:60px;top:0;width:493px;height:140px;background:linear-gradient(100deg,#e0a020,#8a6a20 45%,#2a2a2a 65%,#0e0e0e)"></div>
  <svg class="page-art" viewBox="0 0 553 716" aria-hidden="true">
    <defs>
      <linearGradient id="swoosh2" x1="0" y1="0" x2="1" y2="0">
        <stop offset="0" stop-color="#f04a24"/><stop offset="1" stop-color="#b3141b"/>
      </linearGradient>
    </defs>
    <path d="M0 0 H70 C40 50 60 95 140 105 C260 118 400 100 553 120 V150 C400 130 240 130 0 148 Z" fill="url(#swoosh2)"/>
    <path d="M0 148 C240 128 400 128 553 150 V160 H0 Z" fill="#fff"/>
  </svg>

  <h1 class="heading-coverage">STANDARD COVERAGES FOR<br>YOUR BUSINESS</h1>

  <div class="coverage" style="left:34px;top:241px">
    <div class="coverage-icon"><svg viewBox="0 0 32 32"><circle cx="20" cy="9" r="5"/><path d="M6 28l6-8 4 3 4-8M4 20l6-4"/></svg></div>
    <div><h3>General Liability</h3><p>Covers legal liability associated with your business operations, including bodily harm to other people or damage to their property.</p></div>
  </div>
  <div class="coverage" style="left:282px;top:241px">
    <div class="coverage-icon"><svg viewBox="0 0 32 32"><path d="M5 20l3-8h16l3 8v5H5z"/><path d="M5 20h22"/><circle cx="10" cy="23" r="1"/><circle cx="22" cy="23" r="1"/></svg></div>
    <div><h3>Auto</h3><p>Covers physical damage to your company vehicles, as well as legal liability in the case of auto accidents.</p></div>
  </div>
  <div class="coverage" style="left:34px;top:306px">
    <div class="coverage-icon"><svg viewBox="0 0 32 32"><path d="M4 16L16 5l12 11M7 14v13h18V14M13 27v-7h6v7"/></svg></div>
    <div><h3>FF&amp;E, Property</h3><p>Covers your business-owned buildings and business personal property from damages caused by a covered loss, such as fire, storms, vandalism, theft or water damage.</p></div>
  </div>
  <div class="coverage" style="left:282px;top:306px">
    <div class="coverage-icon"><svg viewBox="0 0 32 32"><path d="M16 4l10 4v7c0 7-5 11-10 13-5-2-10-6-10-13V8z"/><path d="M12 16l3 3 5-6"/></svg></div>
    <div><h3>Cyber</h3><p>Covers the cost of notifying affected individuals, managing public relations and securing legal defense if sensitive data is hacked, lost or stolen.</p></div>
  </div>
  <div class="coverage" style="left:34px;top:372px">
    <div class="coverage-icon"><svg viewBox="0 0 32 32"><path d="M12 6h8l-2 4c5 2 7 6 7 10 0 5-4 7-9 7s-9-2-9-7c0-4 2-8 7-10z"/><path d="M16 14v9M13 17h5a2 2 0 010 3h-4"/></svg></div>
    <div><h3>Workers Compensation</h3><p>Helps cover medical expenses, lost wages and return to work support for employees who are injured on the job.</p></div>
  </div>
  <div class="coverage" style="left:282px;top:372px">
    <div class="coverage-icon"><svg viewBox="0 0 32 32"><circle cx="18" cy="14" r="7"/><circle cx="18" cy="14" r="2.5"/><path d="M6 8v18M6 12h5M6 20h5"/></svg></div>
    <div><h3>Bonds</h3><p>We have worked for many years to cultivate only the best industry relationships so that you don't have to.</p></div>
  </div>
  <div class="coverage" style="left:34px;top:437px">
    <div class="coverage-icon"><svg viewBox="0 0 32 32"><path d="M3 16a13 11 0 0126 0zM16 16v9a3 3 0 01-6 0M16 3v2"/></svg></div>
    <div><h3>Umbrella</h3><p>Provides additional protection above your commercial auto and general liability limits in the event of a large claim or lawsuit.</p></div>
  </div>
  <div class="coverage" style="left:282px;top:437px">
    <div class="coverage-icon"><svg viewBox="0 0 32 32"><circle cx="16" cy="16" r="12"/><path d="M16 8l6 6h-4v8h-4v-8h-4z"/></svg></div>
    <div><h3>EPLI</h3><p>provides coverage if you're sued by an employee, patron or vendor alleging discrimination, sexual harassment, wrongful termination or other types of claims relating to your employment practices.</p></div>
  </div>
  <div class="coverage" style="left:34px;top:503px">
    <div class="coverage-icon"><svg viewBox="0 0 32 32"><path d="M13 3h6v6l3 4v15H10V13l3-4z"/><circle cx="16" cy="20" r="3"/></svg></div>
    <div><h3>Liquor Liability</h3><p>Protects against lawsuits resulting from overconsumption, whether or not the incident occurred on your premises.</p></div>
  </div>

  <div class="carriers">
    <h2 class="carriers-title">CARRIERS</h2>
    <div class="carrier-grid">
      <span class="carrier">THE WEXMOOR</span>
      <span class="carrier">BASTION<br>GROUP</span>
      <span class="carrier">Ferrow Common</span>
      <span class="carrier">WAYFARERS<br>RouteSense</span>
      <span class="carrier">PLAINS MOTOR</span>
      <span class="carrier">Quorra</span>
      <span class="carrier">DELVA</span>
      <span class="carrier">Holloway</span>
      <span class="carrier">CountyFirst</span>
      <span class="carrier">KTO<br>STEADY WORKS</span>
      <span class="carrier">ARVON</span>
      <span class="carrier">Kestrel Home</span>
    </div>
  </div>
  <div class="footer-band"></div>
</section>

</body>
</html>
```